MAREK DOLVANE FOR CONGRESS DISTRICT 32

I need to create a campaign flyer for my congress campaign. I am running for congress in District 32 of Texas as a republican. I am a former Olympic athlete, world champion fencer, Army veteran, Counterintelligence officer (I catch spies).
I want just my first name MAREK in big letters at the top. I want it to say MAREK and below it Republican for Congress.
www.marekforcongress.example

Industry/Entity Type

Political

Colors
EB3D1F
EC4F4E
F09395
F8D3D4
FCEDEE

Requirements
Nice to have
• Would love a catchy title for the Flyer like "Spy Catcher", "Olympic Athlete" "World Champion Fencer" running for Congress in your District!

```html
<!DOCTYPE html>
<html lang="en">
<head>
<meta charset="utf-8">
<title>Marek for Congress – District 32</title>
<link rel="stylesheet" href="https://fonts.googleapis.com/css2?family=Montserrat:wght@700;800;900&family=Oswald:wght@600&display=swap">
<style>
  :root{
    --navy:#1f2e63;
    --navy-dark:#111c45;
    --navy-light:#1c4a92;
    --red:#e8253f;
    --red-dark:#b01e2e;
    --white:#ffffff;
    --stage:#a7a8ab;
    --photo-light:#eceef1;
    --photo-mid:#c9ccd2;
  }
  *{box-sizing:border-box;margin:0;padding:0}
  html,body{width:919px;height:1200px;overflow:hidden;background:var(--stage)}
  .flyer{position:absolute;left:35px;top:0;width:848px;height:1200px;background:var(--white);overflow:hidden;font-family:"Montserrat",sans-serif}
  .top-band{position:absolute;left:0;top:0;width:100%;height:129px;background:linear-gradient(90deg,var(--navy-dark),var(--navy) 50%,var(--navy-light))}
  .top-band svg{position:absolute;left:0;top:0}
  .vote-for{position:absolute;left:287px;top:97px;width:274px;height:56px;background:var(--red);border-bottom:5px solid var(--red-dark);color:var(--white);font-weight:900;font-size:41px;line-height:52px;text-align:center;letter-spacing:0.5px;z-index:3}
  .candidate-name{position:absolute;left:108px;top:140px;font-family:"Oswald",sans-serif;font-weight:600;font-size:158px;line-height:180px;color:var(--navy);letter-spacing:-4px;white-space:nowrap;z-index:1}
  .party{position:absolute;left:112px;top:312px;font-weight:900;font-size:26px;line-height:34px;color:var(--red);letter-spacing:0.3px;white-space:nowrap;z-index:3}
  .flag-art{position:absolute;left:101px;top:362px;width:375px;height:280px;background:linear-gradient(90deg,var(--navy) 0 60%,var(--red) 60% 100%);opacity:.92;z-index:1}
  .athlete-photo{position:absolute;left:290px;top:263px;width:474px;height:378px;background:radial-gradient(ellipse at 60% 40%,var(--photo-light),var(--photo-mid));clip-path:polygon(275px 0,474px 0,474px 378px,110px 378px,110px 170px,275px 110px);z-index:2}
  .headline{position:absolute;left:0;top:628px;width:100%;text-align:center;font-weight:900;font-size:138px;line-height:140px;color:var(--red);letter-spacing:-1px;z-index:3}
  .subhead{position:absolute;left:264px;top:757px;width:320px;height:58px;background:linear-gradient(90deg,var(--navy-dark),var(--navy-light));color:var(--white);font-weight:900;font-size:46px;line-height:58px;text-align:center;letter-spacing:1px}
  .district{position:absolute;left:0;top:824px;width:100%;text-align:center;font-weight:800;font-size:29px;line-height:38px;color:var(--red)}
  .credential{position:absolute;height:80px;background:var(--navy);border-left:7px solid var(--red);color:var(--white);font-weight:800;font-size:21px;line-height:26px;padding:14px 0 0 17px;text-transform:uppercase}
  .credential .badge-star{position:absolute;right:-30px;top:-6px}
  .cred-olympic{left:93px;top:877px;width:231px}
  .cred-fencer{left:364px;top:877px;width:394px}
  .cred-army{left:93px;top:977px;width:231px}
  .cred-intel{left:364px;top:977px;width:394px}
  .crowd-edge{position:absolute;left:0;top:1090px;width:100%;height:28px;background:linear-gradient(180deg,rgba(232,37,63,0) 0%,var(--red) 100%)}
  .footer{position:absolute;left:0;top:1116px;width:100%;height:84px;background:linear-gradient(180deg,var(--red),var(--red-dark));color:var(--white);font-weight:900;font-size:27px;line-height:76px;text-align:center;letter-spacing:1.5px;text-transform:uppercase}
</style>
</head>
<body>
<main class="flyer">
  <header class="top-band">
    <svg width="848" height="129" viewBox="0 0 848 129" aria-hidden="true">
      <defs>
        <polygon id="star" points="0,-25 5.9,-8.1 23.8,-7.7 9.5,3.1 14.7,20.2 0,10 -14.7,20.2 -9.5,3.1 -23.8,-7.7 -5.9,-8.1" fill="#fff"/>
      </defs>
      <use href="#star" x="102" y="54"/>
      <use href="#star" x="209" y="54"/>
      <use href="#star" x="317" y="54"/>
      <use href="#star" x="424" y="54"/>
      <use href="#star" x="532" y="54"/>
      <use href="#star" x="639" y="54"/>
      <use href="#star" x="746" y="54"/>
    </svg>
  </header>
  <div class="vote-for">VOTE FOR</div>
  <h1 class="candidate-name">Marek</h1>
  <p class="party">REPUBLICAN FOR CONGRESS</p>
  <div class="flag-art" role="img" aria-label="Distressed American flag illustration"></div>
  <div class="athlete-photo" role="img" aria-label="Photo of the candidate in fencing whites, holding a foil and mask, shouting in celebration"></div>
  <h2 class="headline">OLYMPIC</h2>
  <div class="subhead">ATHLETE</div>
  <p class="district">Congress, District 32, Texas</p>

  <svg width="0" height="0" style="position:absolute" aria-hidden="true">
    <defs>
      <polygon id="badge" points="37,4 45.5,28 71,28.5 50.5,44 58,69 37,54 16,69 23.5,44 3,28.5 28.5,28" fill="#fff" stroke="#e8253f" stroke-width="2.5" stroke-linejoin="miter"/>
    </defs>
  </svg>

  <div class="credential cred-olympic">Olympic<br>Athlete
    <svg class="badge-star" width="74" height="92" viewBox="0 0 74 74" aria-hidden="true"><use href="#badge"/></svg></div>
  <div class="credential cred-fencer">World Champion<br>Fencer
    <svg class="badge-star" width="74" height="92" viewBox="0 0 74 74" aria-hidden="true"><use href="#badge"/></svg></div>
  <div class="credential cred-army">Army<br>Veteran
    <svg class="badge-star" width="74" height="92" viewBox="0 0 74 74" aria-hidden="true"><use href="#badge"/></svg></div>
  <div class="credential cred-intel">Counterintelligence<br>Officer
    <svg class="badge-star" width="74" height="92" viewBox="0 0 74 74" aria-hidden="true"><use href="#badge"/></svg></div>

  <div class="crowd-edge" role="img" aria-label="Red silhouette of a cheering crowd"></div>
  <footer class="footer">www.marekforcongress.example</footer>
</main>
</body>
</html>
```